I am seeking a book cover design for a new book series. The book deals with life and the principles and essentials that we must have in our lives in order to be happy and have a successful life. Some of the tenets will include 'Spirit' Believe' 'Trust' 'Harmony' 'Family' etc...

I would like to have some natural scene in the background (i.e. water, moutains, forest...that is a ZEN or purity feel)

The '24' should be pronounced in the title in within the foreground of the book cover.

I am open to colors but would like the coloring to emphasize attention. Colors such as forest greens, peaches, pomegranites, are ones that come to mind but i am completely open since it must fit the design.

I will also be looking to do a web design and other additional logos/designs in the coming months so this is a long term opportunity with the right design and communication. I look forward to working with a great partner on this project.

Project Deadline Extended
Reason: I am extending the deadline to allow designers who inquired to get their designs submitted. Also to allow several designers to submit changes to their design.

Target Market(s)

Spiritual - Age range 18-80 - Forward Thinkers - Degreed - All cultures and religions

Industry/Entity Type

Communication

Requirements
Must have
• The title 'The 17 Keystones of Being'

My Name as the Author: Dorian Pellwick

the thoughts should also include a backcover copy consistent with the front and a theme design for the Series.
The book is expected to be 5 1/2 x 8 1/2"
Nice to have
• The book will be released in a series format as well as the entire 17 Keystones. As a suggestion, the books released as part of an individual essential would have the name of that essential referenced on the book. Example (BELEIVE). You may take that into consideration when designing for he cover. Thank you.

```html
<!DOCTYPE html>
<html lang="en">
<head>
<meta charset="utf-8">
<title>The 17 Keystones of Being — Cover Spread</title>
<link href="https://fonts.googleapis.com/css2?family=Cinzel:wght@400;500&family=EB+Garamond&family=Questrial&family=Arimo:wght@700&display=swap" rel="stylesheet">
<style>
  :root {
    --bark: #3d2a1b;
    --ochre: #9e761b;
    --gold: #d6b552;
    --white: #ffffff;
    --ink: #3a2a1c;
    --leaf-light: #e8a544;
    --leaf-mid: #c97a22;
    --leaf-deep: #8a4d17;
    --trunk: #6b5a45;
  }
  * { margin: 0; padding: 0; box-sizing: border-box; }
  html, body { width: 1200px; height: 850px; overflow: hidden; background: var(--white); }
  .spread { position: relative; width: 1200px; height: 850px; overflow: hidden; }

  .forest-strip {
    position: absolute; left: 0; top: 0; width: 127px; height: 850px;
    background: linear-gradient(180deg, var(--leaf-mid) 0%, var(--leaf-light) 30%, var(--leaf-mid) 60%, var(--leaf-deep) 100%);
  }
  .back-panel {
    position: absolute; left: 127px; top: 0; width: 428px; height: 850px;
    background: var(--ochre);
  }
  .back-copy {
    position: absolute; left: 35px; top: 222px; width: 350px;
    font-family: "EB Garamond", Georgia, serif; font-size: 15.5px; line-height: 30.6px;
    color: var(--white);
  }
  .back-copy p + p { margin-top: 30.6px; }

  .spine {
    position: absolute; left: 555px; top: 0; width: 96px; height: 850px;
    background: var(--bark);
  }
  .spine-title {
    position: absolute; left: 50%; top: 282px; width: 300px; height: 80px;
    transform: translate(-50%, -50%) rotate(-90deg);
    display: flex; align-items: center; justify-content: flex-start;
    color: var(--white); font-family: "Cinzel", serif;
  }
  .spine-title .the { font-size: 14px; letter-spacing: 1px; align-self: flex-end; margin-bottom: 16px; }
  .spine-title .num { font-size: 96px; line-height: 1; margin: 0 4px 0 2px; }
  .spine-title .words { display: flex; flex-direction: column; line-height: 1; }
  .spine-title .w1 { font-size: 25px; letter-spacing: 1px; }
  .spine-title .w2 { font-size: 34px; letter-spacing: 1px; margin-top: 2px; }
  .spine-author {
    position: absolute; left: 50%; top: 705px;
    transform: translate(-50%, -50%) rotate(-90deg);
    font-family: "Arimo", Arial, sans-serif; font-weight: 700; font-size: 17px;
    color: var(--gold); white-space: nowrap; letter-spacing: 0.5px;
  }

  .front {
    position: absolute; left: 651px; top: 0; width: 549px; height: 850px;
  }
  .front-band { position: absolute; left: 0; top: 0; width: 549px; height: 200px; background: var(--bark); }
  .front-photo {
    position: absolute; left: 0; top: 200px; width: 549px; height: 650px;
    background:
      linear-gradient(90deg, rgba(107,90,69,0.35) 0%, rgba(0,0,0,0) 20%, rgba(107,90,69,0.3) 45%, rgba(0,0,0,0) 60%, rgba(107,90,69,0.35) 80%, rgba(0,0,0,0) 100%),
      linear-gradient(180deg, #e9c48a 0%, var(--leaf-light) 25%, var(--leaf-mid) 65%, var(--leaf-deep) 100%);
  }
  .front-title { position: absolute; left: 0; top: 0; color: var(--white); font-family: "Cinzel", serif; }
  .front-title .the {
    position: absolute; left: 47px; top: 88px; transform: rotate(-90deg); transform-origin: center;
    color: var(--gold); font-size: 28px; letter-spacing: 2px; white-space: nowrap;
    width: 60px; text-align: center; margin-left: -30px; margin-top: -17px;
  }
  .front-title .num { position: absolute; left: 58px; top: 28px; font-size: 170px; line-height: 1; }
  .front-title .w1 { position: absolute; left: 243px; top: 64px; font-size: 46px; letter-spacing: 1px; white-space: nowrap; line-height: 1; }
  .front-title .w2 { position: absolute; left: 243px; top: 112px; font-size: 58px; letter-spacing: 1px; white-space: nowrap; line-height: 1; }

  .series-tag {
    position: absolute; right: 0; top: 238px; width: 234px; height: 30px;
    background: rgba(255,255,255,0.82);
    font-family: "Questrial", sans-serif; font-size: 17px; letter-spacing: 2px;
    color: var(--ink); display: flex; align-items: center; padding-left: 36px;
  }
  .front-author {
    position: absolute; left: 315px; top: 765px;
    font-family: "Arimo", Arial, sans-serif; font-weight: 700; font-size: 22px;
    color: var(--white); white-space: nowrap; letter-spacing: 0.3px;
  }
</style>
</head>
<body>
<main class="spread">
  <div class="forest-strip" role="img" aria-label="Photograph of an autumn beech forest with golden orange leaves"></div>

  <section class="back-panel">
    <div class="back-copy">
      <p>Lorem ipsum dolor sit amet, consectetur adipiscing elit. Nullam fermentum imperdiet bibendum. Nulla facilisi. Nunc leo diam, sollicitudin fermentum venenatis ut, gravida eu odio. Nullam posuere pellentesque mauris et blandit. Duis eu est ut ipsum faucibus pellentesque. Vivamus ut commodo quam. Vivamus vel libero dolor. Nulla dapibus auctor lacus quis malesuada.</p>
      <p>Proin accumsan tincidunt odio, eget ullamcorper turpis volutpat in. Proin enim tellus, accumsan non rhoncus ut, condimentum sit amet mi. Duis ligula nisl, interdum vel venenatis sed, gravida non justo. Morbi convallis laoreet dignissim.</p>
    </div>
  </section>

  <section class="spine">
    <div class="spine-title">
      <span class="the">THE</span>
      <span class="num">17</span>
      <span class="words"><span class="w1">KEYSTONES</span><span class="w2">OF BEING</span></span>
    </div>
    <div class="spine-author">Dorian Pellwick</div>
  </section>

  <section class="front">
    <div class="front-band"></div>
    <div class="front-photo" role="img" aria-label="Photograph of tall beech trunks in an autumn forest with orange foliage and a leaf-covered floor"></div>
    <h1 class="front-title">
      <span class="the">THE</span>
      <span class="num">17</span>
      <span class="w1">KEYSTONES</span>
      <span class="w2">OF BEING</span>
    </h1>
    <div class="series-tag">Harmony</div>
    <div class="front-author">Dorian Pellwick</div>
  </section>
</main>
</body>
</html>
```